New design for a physiotherapy clinic specializing in laser therapy

BrightPath Physiotherapy is a unique clinic specializing in laser therapy. The clinic is now 7 years old and has a well established reputation for patient care.

We are the largest laser physiotherapy clinic in Mississauga, ON, Canada. We use state of the art laser therapy equipment. Our knowledge base of how to use Low Level Laser Therapy in conjunction with traditional physiotherapy is what sets us apart. Nobody wants to live with pain and everyone wants to get better as quickly as possible. Our treatment methodology helps our patients return to normal lives quickly.

We want a website that communicates expertise, trust and shows that we care for our patients. We also want people to understand that the treatments are painless and speed up healing naturally.
Updates

Please include a location tab in your submission.  This page should have a map of our location and our phone number.

I do not want any white coat and stethoscope people. We do not see hospitalized patients. We use Zorva-Kel NuvaQuill laser web site www.nuvaquilllaser.example please remove any images with other laser machines. I do not want "massage" therapy pictures as the main image. We treat post op total hip and knee replacements, rotator cuff injuries, osteoarthritic back pain patients, sprained ankles, degenerative disc disease problems as some of the more general injuries seen.

Industry/Entity Type

Clinic

Requirements
Must have
• We want to retain as much of the current content as possible. We will be looking at editing the content to make it shorter.

In addition to the current pages we want to add a blog page and link.

see our current site www.brightpathphysio.example
Nice to have
• Medical Images in the Whiplash and Auto Injuries should be re-drawn.

We want a clean, uncluttered look to the site.

Should not have
• Do not use illustrations of lasers shooting out or cutting. This is a "Cold" laser and does not cut. The laser procedure is gentle and soothing.

```html
<!DOCTYPE html>
<html lang="en">
<head>
<meta charset="utf-8">
<title>BrightPath Physiotherapy Inc.</title>
<link rel="stylesheet" href="https://fonts.googleapis.com/css2?family=Open+Sans:wght@400;600;700&family=Noto+Serif:wght@700&display=swap">
<style>
  :root {
    --green: #8cc63f;
    --green-nav-top: #94cc5e;
    --green-nav-bottom: #7cb84a;
    --green-divider: #6fa83e;
    --dark: #3b3637;
    --page-bg: #e3e0da;
    --white: #ffffff;
    --grey-text: #8a8886;
    --card-bg: #edebe7;
    --card-active: #8b8687;
    --card-title: #7a756f;
    --card-body: #8b8680;
    --body-text: #4a4a48;
    --title-text: #5a5a54;
    --logo-text: #2f2f2f;
  }
  * { box-sizing: border-box; margin: 0; padding: 0; }
  html, body { width: 1200px; height: 612px; overflow: hidden; }
  body {
    position: relative;
    font-family: "Open Sans", Arial, sans-serif;
    background: var(--page-bg);
  }
  .site-header {
    position: absolute; left: 0; top: 0; width: 1200px; height: 211px;
    background: var(--white);
    border-top: 4px solid var(--green);
    border-bottom: 1px solid #d6d3cc;
  }
  .brand {
    position: absolute; left: 136px; top: 60px;
    display: flex; align-items: center; gap: 16px;
  }
  .brand-dot {
    width: 26px; height: 26px; border-radius: 50%;
    background: var(--green);
  }
  .brand-name {
    font-size: 34px; font-weight: 400; color: var(--logo-text);
    letter-spacing: 1px; line-height: 1.2;
  }
  .main-nav {
    position: absolute; left: 130px; top: 187px; width: 940px; height: 41px;
    background: linear-gradient(var(--green-nav-top), var(--green-nav-bottom));
    border: 1px solid var(--green-divider);
    display: flex;
  }
  .main-nav a {
    display: flex; align-items: center; justify-content: center;
    height: 100%; color: var(--white); font-weight: 700; font-size: 14px;
    text-decoration: none; border-right: 1px solid var(--green-divider);
    letter-spacing: .2px;
  }
  .main-nav a.is-active { background: var(--dark); }
  .submenu {
    position: absolute; left: 206px; top: 228px; width: 228px;
    background: var(--white); border: 1px solid var(--dark); z-index: 3;
  }
  .submenu a {
    display: block; height: 33px; line-height: 32px; padding-left: 10px;
    font-size: 14px; font-weight: 700; color: var(--grey-text);
    text-decoration: none; border-bottom: 1px solid var(--dark);
  }
  .submenu a:last-child { border-bottom: 0; }
  .submenu a.is-active { background: var(--dark); color: var(--white); }
  .content-panel {
    position: absolute; left: 120px; top: 243px; width: 960px; height: 380px;
    background: var(--white);
  }
  .hero {
    position: absolute; left: 130px; top: 255px; width: 620px; height: 338px;
    background: linear-gradient(180deg, #b9cfe0 0%, #d7dde0 22%, #6d7a4e 36%, #8a6a52 46%, #6e5a4a 58%, #9a7f72 70%, #b09890 100%);
  }
  .commitment {
    position: absolute; left: 416px; top: 255px; width: 334px; height: 132px;
    background: rgba(255,255,255,.78); padding: 24px 16px 0 17px;
  }
  .commitment h2 {
    font-family: "Noto Serif", Georgia, serif; font-size: 20px;
    color: var(--title-text); line-height: 1.1; margin-bottom: 4px;
  }
  .commitment p { font-size: 14px; line-height: 19px; color: var(--body-text); }
  .service-list { position: absolute; left: 770px; top: 255px; width: 300px; }
  .service-card {
    position: relative; height: 76px; margin-bottom: 11px;
    background: var(--card-bg); padding: 9px 70px 0 11px;
  }
  .service-card h3 { font-size: 16px; font-weight: 700; color: var(--card-title); line-height: 20px; }
  .service-card p { font-size: 13px; line-height: 16px; color: var(--card-body); }
  .service-card .mark {
    position: absolute; right: 10px; top: 12px; width: 52px; height: 52px;
    border-radius: 50%; border: 4px solid var(--white); opacity: .8;
  }
  .service-card.is-active { background: var(--card-active); }
  .service-card.is-active h3, .service-card.is-active p { color: var(--white); }
  .service-card.is-active .mark { opacity: 1; }
  .content-footer {
    position: absolute; left: 130px; top: 603px; width: 940px; height: 9px;
    background: #ebe9e5;
  }
</style>
</head>
<body>
  <header class="site-header">
    <div class="brand">
      <span class="brand-dot"></span>
      <span class="brand-name">BrightPath Physiotherapy Inc.</span>
    </div>
  </header>

  <nav class="main-nav">
    <a href="#" style="width:76px">Home</a>
    <a href="#" class="is-active" style="width:93px">Services</a>
    <a href="#" style="width:68px">FAQs</a>
    <a href="#" style="width:106px">Insurance</a>
    <a href="#" style="width:126px">Testimonials</a>
    <a href="#" style="width:74px">Media</a>
    <a href="#" style="width:124px">Employment</a>
    <a href="#" style="width:63px">Blog</a>
    <a href="#" style="width:71px">Links</a>
    <a href="#" style="width:109px">Contact Us</a>
  </nav>

  <div class="submenu">
    <a href="#">Physiotherapy</a>
    <a href="#">Laser Therapy</a>
    <a href="#" class="is-active">Whiplash &amp; Auto Injuries</a>
  </div>

  <main class="content-panel"></main>

  <div class="hero" role="img" aria-label="Photo of a runner's legs jogging along a stone seaside path at sunset"></div>

  <section class="commitment">
    <h2>Our Patient Commitment</h2>
    <p>BrightPath Physiotherapy is committed to helping you get better, faster, with fewer treatments.</p>
  </section>

  <aside class="service-list">
    <div class="service-card is-active">
      <h3>Physiotherapy</h3>
      <p>Improving functional independence and physical performance.</p>
      <span class="mark"></span>
    </div>
    <div class="service-card">
      <h3>Laser Therapy</h3>
      <p>Delivering light energy to the cells to assist in the natural healing process.</p>
      <span class="mark"></span>
    </div>
    <div class="service-card">
      <h3>Whiplash &amp; Auto Injuries</h3>
      <p>Our registered physiotherapists assess and treat injuries.</p>
      <span class="mark"></span>
    </div>
    <div class="service-card">
      <h3>Massage Therapy</h3>
      <p>Reduce and prevent stress, tension, and discomfort of injuries.</p>
      <span class="mark"></span>
    </div>
  </aside>

  <div class="content-footer"></div>
</body>
</html>
```